Business card design needed

We are a start up Mobile Vet Clinic.
We will be servicing an are that cover the Gladstone Region Shire.
Bookings will be made via the number listed or email address.
Travel will be charged

Target Market(s)

Pet Owners

Industry/Entity Type

Business

Contact Information for Business Card

BRINDELLA MOBILE VET
Tarrowen Pty Ltd
Dana Fosterby BVSc
27 Wexhaven St
Calliope QLD 4680

PH: 0743186209 Fax: 0743186514 email: bmvet@quillnet.example

Logo styles of interest
Pictorial/Combination Logo

```html
<!DOCTYPE html>
<html lang="en">
<head>
<meta charset="utf-8">
<title>Brindella Mobile Vet – Business Card</title>
<link rel="stylesheet" href="https://fonts.googleapis.com/css2?family=Lato:wght@400&display=swap">
<style>
  :root {
    --paper: #ffffff;
    --orange-light: #f7a83a;
    --orange-mid: #f38b2f;
    --red-orange: #ec4a2a;
    --ink-light: #ffffff;
  }
  html, body {
    margin: 0;
    padding: 0;
    overflow: hidden;
    background: var(--paper);
  }
  .card {
    position: relative;
    width: 1200px;
    height: 667px;
    background: var(--paper);
    overflow: hidden;
    font-family: "Lato", sans-serif;
  }
  .brand-mark {
    position: absolute;
    left: 0;
    top: 150px;
    width: 1200px;
    display: flex;
    align-items: center;
    justify-content: center;
    gap: 28px;
  }
  .brand-dot {
    width: 96px;
    height: 96px;
    border-radius: 50%;
    background: var(--orange-light);
  }
  .brand-name {
    font-size: 58px;
    font-weight: 400;
    letter-spacing: 3px;
    color: var(--orange-mid);
  }
  .info-band {
    position: absolute;
    left: 0;
    top: 328px;
    width: 1200px;
    height: 339px;
    background: linear-gradient(180deg, var(--orange-light) 0%, var(--orange-mid) 35%, var(--red-orange) 100%);
    color: var(--ink-light);
    text-align: center;
  }
  .business-name {
    position: absolute;
    left: 0;
    top: 26px;
    width: 100%;
    margin: 0;
    font-size: 70px;
    font-weight: 400;
    letter-spacing: 2px;
    line-height: 84px;
  }
  .contact-details {
    position: absolute;
    left: 0;
    top: 125px;
    width: 100%;
    font-size: 37px;
    letter-spacing: 1.4px;
    line-height: 52px;
  }
  .contact-details p {
    margin: 0;
    white-space: nowrap;
  }
</style>
</head>
<body>
  <div class="card">
    <div class="brand-mark">
      <span class="brand-dot"></span>
      <span class="brand-name">BRINDELLA</span>
    </div>
    <section class="info-band">
      <h1 class="business-name">BRINDELLA MOBILE VET</h1>
      <div class="contact-details">
        <p class="owner-line">Tarrowen Pty Ltd Dana Fosterby BVSc</p>
        <p class="address-line">27 Wexhaven St Calliope; QLD 4680 PH: 0743186209</p>
        <p class="contact-line">Fax: 0743186514; email: bmvet@quillnet.example</p>
      </div>
    </section>
  </div>
</body>
</html>
```